Animation College website

Name of College: Brightvale School of 3D Animation and VFX

We need a redesigned modern website for Brightvale. The web-design should communicate a VFX and animation school and education. We will also need full access to the website once completed. We will also need access to the website to be able to make changes to the content and site ideally the website would be built on Wordpress.

To learn more about what the College please visit: http://brightvale-academy.example/
The video on the homepage demonstrates why Brightvale is a unique college offering 3D animation and VFX. The direct link to the video can be watched here: https://videohost.example/581047293

Client Profile Summary: Brightvale is an improved concept in job skills training for the 3D animation and visual effects industries. Our high graduate job placement numbers are based on the assertion that job skills must include more than simply learning to use software tools. Where nearly every digital media program teaches tools, job skills training should be about learning how to do a job in addition to learning how to use software tools. Brightvale is taught in an apprenticeship style with very experienced faculty mentoring and teaching students to learn how to master their craft (VFX and animation) so they can seamlessly step into industry and excel.

Target Market(s)

High school students, students interested in learning about animation and 3D.

Industry/Entity Type

College

Coding

Coded - Design and coding required

Number of Pages Required

5+ page

Font styles to use
Sans Serif

Colors

Designer to choose colors to be used in the design.

Requirements
Must have
• Please include the video on the current Brightvale-academy.example website. https://videohost.example/581047293
• Use the same content on the current brightvale-academy.example website.
• Include a page to showcase student work.
• Website must also be mobile responsive.
Should not have
• The attached PDF of the landing page is just an example of something we like. You do not have to replicate this. The PDF landing page is showing the colour blue you should incorporate.

```html
<!DOCTYPE html>
<html lang="en">
<head>
<meta charset="utf-8">
<title>Brightvale School of 3D Animation and VFX – One-Year Intensive Training Program</title>
<link rel="stylesheet" href="https://fonts.googleapis.com/css2?family=Open+Sans:ital,wght@0,400;0,600;0,700;1,400;1,600&family=Nunito+Sans:wght@600;700;800&display=swap">
<style>
:root{
  --blue:#1b72b8;
  --blue-deep:#1a66a6;
  --blue-btn:#1f78c1;
  --ink:#222428;
  --ink-soft:#3b3e44;
  --text:#5c6067;
  --white:#ffffff;
  --dark:#1a1b1d;
  --panel:rgba(16,18,22,.82);
  --rule:rgba(255,255,255,.35);
}
*{box-sizing:border-box;margin:0;padding:0}
html,body{width:1200px;height:3186px;overflow:hidden}
body{font-family:"Open Sans",Arial,sans-serif;color:var(--text);background:var(--white);position:relative}
.section{position:absolute;left:0;width:1200px}
.abs{position:absolute}

/* Hero */
.hero{top:0;height:597px}
.hero-photo{position:absolute;inset:0;background:
  radial-gradient(ellipse at 48% 28%,rgba(150,170,190,.55),transparent 40%),
  radial-gradient(ellipse at 20% 80%,rgba(90,70,50,.5),transparent 45%),
  linear-gradient(180deg,#2c3036 0%,#1d1f23 55%,#141516 100%)}
.brand{left:98px;top:22px;display:flex;align-items:center;gap:14px;font-family:"Nunito Sans",Arial,sans-serif;font-weight:800;font-size:34px;color:var(--white);letter-spacing:.5px}
.brand-mark{width:64px;height:64px;border-radius:50%;background:var(--blue-btn)}
.nav{right:100px;top:38px;display:flex;gap:20px;align-items:center;font-family:"Nunito Sans",Arial,sans-serif;font-weight:700;font-size:17px;color:var(--white)}
.hero-title{left:98px;top:300px;font-family:"Nunito Sans",Arial,sans-serif;font-weight:800;font-size:35px;line-height:44px;color:var(--white)}
.hero-sub{left:98px;top:455px;font-style:italic;font-weight:600;font-size:19.5px;color:var(--white)}
.form-panel{left:703px;top:117px;width:397px;height:480px;background:var(--panel);border:2px solid rgba(255,255,255,.7);border-bottom:none;padding:0 26px}
.form-title{text-align:center;margin-top:10px;font-family:"Nunito Sans",Arial,sans-serif;font-weight:800;font-size:21px;color:var(--white)}
.form-note{text-align:center;margin-top:24px;font-size:14.5px;line-height:26px;color:var(--white)}
.field{height:29px;background:var(--white);margin-top:12.5px;font-size:12.5px;color:#555;padding:6px 8px}
.field:first-of-type{margin-top:13px}
.field.area{height:70px}
.form-btn{display:block;margin:18px auto 0;width:180px;height:43px;border-radius:22px;background:var(--blue-btn);color:var(--white);font-family:"Nunito Sans",Arial,sans-serif;font-weight:800;font-size:15px;text-align:center;line-height:43px}

/* Accreditation strip */
.badges{top:597px;height:104px;background:var(--blue);display:flex;justify-content:center;align-items:center;gap:76px}
.badge{width:64px;height:64px;border-radius:50%;background:rgba(255,255,255,.85)}
.badge.square{border-radius:6px;width:72px;height:58px}

/* Text sections */
h2.title{font-family:"Open Sans",Arial,sans-serif;font-weight:700;font-size:29px;line-height:36px;color:var(--ink);text-transform:uppercase;letter-spacing:.2px}
.lead{font-weight:600;font-size:19px;color:var(--ink-soft)}
.body{font-size:12.2px;line-height:28px;color:var(--text);width:1000px}

.intro{top:701px;height:333px}
.video-band{top:1034px;height:461px;background:
  radial-gradient(ellipse at 10% 40%,rgba(120,100,90,.5),transparent 40%),
  radial-gradient(ellipse at 90% 60%,rgba(120,110,100,.45),transparent 40%),
  linear-gradient(180deg,#2b2b2d,#1e1f21)}
.video-frame{left:314px;top:53px;width:572px;height:353px;border:3px solid var(--white);background:#0d0d0e}
.video-bar{height:38px;background:#111;color:#e6e6e6;text-align:center;font-size:20px;line-height:38px}
.video-still{position:absolute;left:0;top:38px;right:0;bottom:38px;background:linear-gradient(90deg,#3a3a3c,#8a8a8c 70%,#5a5a5c)}
.play{position:absolute;left:50%;top:50%;width:56px;height:56px;margin:-28px 0 0 -28px;border-radius:50%;background:rgba(0,0,0,.75)}

.learn{top:1495px;height:461px}
.steps{font-size:12.2px;line-height:28.5px;color:var(--text)}

.testimonial{top:1956px;height:444px;background:linear-gradient(135deg,var(--blue) 0%,var(--blue-deep) 100%);color:var(--white)}
.avatar{left:539px;top:64px;width:124px;height:124px;border-radius:50%;border:4px solid var(--white);background:linear-gradient(180deg,#b48b6e,#6b4a3a)}
.quote{left:250px;top:220px;width:700px;text-align:center;font-style:italic;font-size:13.8px;line-height:29px}
.q-name{left:0;width:1200px;top:328px;text-align:center;font-weight:700;font-size:17.5px}
.q-role{left:0;width:1200px;top:370px;text-align:center;font-size:13px}
.qmark{font-family:"Open Sans",Arial,sans-serif;font-weight:700;font-size:150px;line-height:1;color:rgba(255,255,255,.35)}

.advantage{top:2400px;height:537px}
.ticks{list-style:none;font-size:12.2px;color:var(--text)}
.ticks li{display:flex;align-items:center;gap:12px;height:28.3px}

.footer{top:2937px;height:249px;background:linear-gradient(180deg,#242527,#171819);color:var(--white)}
.footer-title{left:0;width:1200px;top:56px;text-align:center;font-family:"Nunito Sans",Arial,sans-serif;font-weight:800;font-size:29px}
.footer-sub{left:0;width:1200px;top:107px;text-align:center;font-weight:600;font-size:17px}
.footer-rule{left:98px;top:168px;width:1004px;height:1px;background:var(--rule)}
.copyright{left:98px;top:196px;font-size:12.5px}
.social{left:944px;top:188px;display:flex;gap:15px}
.social span{width:36px;height:36px;border-radius:50%;border:2px solid var(--white)}
</style>
</head>
<body>

<header class="section hero">
  <div class="hero-photo" role="img" aria-label="Students working at animation workstations with multiple monitors"></div>
  <div class="abs brand"><span class="brand-mark"></span>Brightvale</div>
  <nav class="abs nav">
    <span>How to Pick a School</span><span>Admission</span><span>Training</span><span>Philosophy</span><span>Faculty &amp; Staff</span><span>Apply</span><span>Blog</span>
    <svg width="16" height="16" viewBox="0 0 16 16" aria-label="Search"><circle cx="6.5" cy="6.5" r="5" fill="none" stroke="#fff" stroke-width="2.2"/><line x1="10.2" y1="10.2" x2="15" y2="15" stroke="#fff" stroke-width="2.4"/></svg>
  </nav>
  <h1 class="abs hero-title">3D ANIMATION &amp;<br>VFX ONE-YEAR INTENSIVE<br>TRAINING PROGRAM</h1>
  <p class="abs hero-sub">Train Alongside Passionate and Experienced Industry Masters</p>
  <form class="abs form-panel">
    <div class="form-title">WANT TO KNOW MORE?</div>
    <p class="form-note">Complete this form to receive more information<br>about program details &amp; more!</p>
    <div class="field">First Name*</div>
    <div class="field">Last Name*</div>
    <div class="field">Phone*</div>
    <div class="field">Email*</div>
    <div class="field">Country of Residence*</div>
    <div class="field area">Comments</div>
    <span class="form-btn">SEND ME FREE INFO</span>
  </form>
</header>

<section class="section badges" aria-label="Accreditations">
  <span class="badge"></span><span class="badge"></span><span class="badge"></span><span class="badge square"></span><span class="badge square"></span>
</section>

<section class="section intro">
  <h2 class="abs title" style="left:98px;top:64px">One-Year Intensive Training Program</h2>
  <p class="abs lead" style="left:98px;top:106px">An exciting, comprehensive program with a 100% graduate employment rate</p>
  <p class="abs body" style="left:98px;top:161px">The 48-week Brightvale One-Year Intensive Training Program is designed to provide students the practical skills and real-world experience needed to thrive in the film and TV animation, and VFX industries. Students are mentored by our passionate instructors who have extensive industry experience. Each of our instructors knows exactly what it takes for students to be successful. We carefully crafted the program curriculum to teach students how to function in a real production team so that they can be highly-effective professionals once they enter the workforce.</p>
</section>

<section class="section video-band" role="img" aria-label="Students in a classroom behind the featured video">
  <div class="abs video-frame">
    <div class="video-bar">Brightvale Student Work</div>
    <div class="video-still" role="img" aria-label="Student work video still of spacecraft flying down a trench">
      <svg class="play" viewBox="0 0 56 56"><polygon points="22,17 40,28 22,39" fill="#fff"/></svg>
    </div>
  </div>
</section>

<section class="section learn">
  <h2 class="abs title" style="left:98px;top:67px">Learn Animation &amp; Visual Effects Production<br>From the Experts</h2>
  <p class="abs lead" style="left:98px;top:143px">The world's first and sole simulated production training program</p>
  <p class="abs body" style="left:98px;top:190px">Our philosophy is unique. We don't focus on grades. Instead, we focus on preparing each of our students for the challenges of working as 3D artists such as animators, lighting TDs, riggers, modellers, compositors and more. Our instructors teach you until you're confident in your skills. If you need more help, we train you until you're ready.&nbsp; Students grasp valuable skills that employers are looking for over the course of three intensive terms:</p>
  <ol class="abs steps" style="left:98px;top:311px;list-style:none">
    <li>1. Core Skills: An intensive introduction to skills involving cameras, modeling, animation, dynamics, lighting, composition, production, and more.</li>
    <li>2. Transition into Practice: Expand on core skills with advanced training and team production.</li>
    <li>3. Practical Training: Practical hands-on production and dailies training.</li>
  </ol>
</section>

<section class="section testimonial">
  <div class="abs avatar" role="img" aria-label="Portrait of graduate Dana Whitfield"></div>
  <span class="abs qmark" style="left:212px;top:100px">&ldquo;</span>
  <span class="abs qmark" style="left:904px;top:248px">&rdquo;</span>
  <p class="abs quote">I was able to get my 1st job only two weeks after finishing this program It is the future of VFX training Brightvale has changed my life and changed the way that I think about the world around me I would highly recommend this program above any other, to anyone wishing to pursue a career in the film industry</p>
  <p class="abs q-name">Dana Whitfield</p>
  <p class="abs q-role">Lighting Artist Graduate</p>
</section>

<section class="section advantage">
  <h2 class="abs title" style="left:98px;top:67px">The Brightvale Advantage</h2>
  <p class="abs lead" style="left:98px;top:110px">A program designed by industry, for industry</p>
  <p class="abs body" style="left:98px;top:160px">There's a reason why each of our graduates have found work in their field. We don't sell courses, we provide relevant training.&nbsp; In order to bring out the best in our students, we run a program that we know will maximize each student's potential. Brightvale offers an un-paralleled training experience. Here are a few examples of what makes our school unique:</p>
  <ul class="abs ticks" style="left:96px;top:279px">
    <li><svg width="15" height="15" viewBox="0 0 15 15"><circle cx="7.5" cy="7.5" r="7.5" fill="#1f78c1"/><polyline points="4,7.8 6.5,10.2 11,5" fill="none" stroke="#fff" stroke-width="1.8"/></svg>Affordable tuition for both domestic and international students</li>
    <li><svg width="15" height="15" viewBox="0 0 15 15"><circle cx="7.5" cy="7.5" r="7.5" fill="#1f78c1"/><polyline points="4,7.8 6.5,10.2 11,5" fill="none" stroke="#fff" stroke-width="1.8"/></svg>A faculty of 12 world-class industry masters</li>
    <li><svg width="15" height="15" viewBox="0 0 15 15"><circle cx="7.5" cy="7.5" r="7.5" fill="#1f78c1"/><polyline points="4,7.8 6.5,10.2 11,5" fill="none" stroke="#fff" stroke-width="1.8"/></svg>Maximum class size of 12 students</li>
    <li><svg width="15" height="15" viewBox="0 0 15 15"><circle cx="7.5" cy="7.5" r="7.5" fill="#1f78c1"/><polyline points="4,7.8 6.5,10.2 11,5" fill="none" stroke="#fff" stroke-width="1.8"/></svg>One-on-one mentorship</li>
    <li><svg width="15" height="15" viewBox="0 0 15 15"><circle cx="7.5" cy="7.5" r="7.5" fill="#1f78c1"/><polyline points="4,7.8 6.5,10.2 11,5" fill="none" stroke="#fff" stroke-width="1.8"/></svg>Employment opportunities</li>
    <li><svg width="15" height="15" viewBox="0 0 15 15"><circle cx="7.5" cy="7.5" r="7.5" fill="#1f78c1"/><polyline points="4,7.8 6.5,10.2 11,5" fill="none" stroke="#fff" stroke-width="1.8"/></svg>Scholarships</li>
    <li><svg width="15" height="15" viewBox="0 0 15 15"><circle cx="7.5" cy="7.5" r="7.5" fill="#1f78c1"/><polyline points="4,7.8 6.5,10.2 11,5" fill="none" stroke="#fff" stroke-width="1.8"/></svg>And more!</li>
  </ul>
</section>

<footer class="section footer">
  <p class="abs footer-title">WANT TO LEARN MORE?</p>
  <p class="abs footer-sub">Fill out the form above to receive information about the program</p>
  <div class="abs footer-rule"></div>
  <p class="abs copyright">© Copyright 2017, Brightvale School Of 3D Animation &amp; VFX. All Rights Reserved.</p>
  <div class="abs social" aria-label="Social links"><span></span><span></span><span></span><span></span></div>
</footer>

</body>
</html>
```